Startup Biz for Seniors needs your help!

Our business is a Startup that Employs Caregivers to do IN HOME Care of the Elderly. Our website is not yet running. But, a business similar to ours is Tallbrookcare.com

We are looking for a card that only has 4 Elements:
-Logo
- Website
- Tag Line
- Phone
We would like to see some eye catching backgrounds.
We would like to see some designs with and some without a Photo.
Would like the Photo to be of a Caregiver taking care of a Senior. The photo should show both of them smiling.

Target Market(s)

Age 35-55 who has Parents that are Elderly and need care

Industry/Entity Type

Home Health Care

Contact Information for Business Card

Want it to Pop Out to the viewer . Thinking maybe:
Side 1: LOGO with Website & Tag line
Side 2: Phone Number

Font styles to use
Other font styles liked:
• Same Font as our Logo

Colors

Designer to choose colors to be used in the design.

Requirements
Must have
• Logo, website, Tag Line, Phone number and Email: "info@velvetdays.example"
• Please use one of the photos that I have attached.
Nice to have
• Would like to see a Photo worked in that has a Care Taker taking care of an Elderly Person and they are both smiling.

```html
<!DOCTYPE html>
<html lang="en">
<head>
<meta charset="utf-8">
<title>Velvet Days – Business Card</title>
<link rel="stylesheet" href="https://fonts.googleapis.com/css2?family=Fredoka:wght@600&family=Roboto:wght@400;500&display=swap">
<style>
  :root{
    --stage:#2a2a2c;
    --card:#ffffff;
    --brand-blue:#1d4f9c;
    --brand-orange:#ee5a24;
    --text-grey:#555a60;
    --rule:#c9ccd1;
    --photo-light:#f2f2ee;
    --photo-mid:#d9d2c6;
    --photo-warm:#c2ab8f;
  }
  *{box-sizing:border-box;margin:0;padding:0}
  html,body{width:1200px;height:801px;overflow:hidden;background:var(--stage)}
  .stage{width:1200px;height:801px;display:flex;flex-direction:column;align-items:center;justify-content:center;gap:30px}
  .card{width:620px;height:354px;background:var(--card);position:relative;overflow:hidden;box-shadow:0 10px 30px rgba(0,0,0,.45)}

  /* front */
  .front-photo{position:absolute;inset:0;background:linear-gradient(95deg,#ffffff 0%,#ffffff 22%,var(--photo-light) 38%,var(--photo-mid) 65%,var(--photo-warm) 100%)}
  .front-brand{position:absolute;left:40px;top:0;bottom:0;width:230px;display:flex;flex-direction:column;align-items:center;justify-content:center;gap:12px}
  .front-brand .mark{width:112px;height:112px;border-radius:50%;background:var(--brand-orange)}
  .front-brand .wordmark{font-family:'Fredoka',sans-serif;font-weight:600;font-size:34px;color:var(--brand-blue);line-height:1;white-space:nowrap}
  .front-brand .website{font-family:'Roboto',sans-serif;font-size:13px;letter-spacing:2px;color:var(--text-grey);margin-top:-4px;white-space:nowrap}

  /* back */
  .card--back{display:flex;align-items:center}
  .back-brand{width:52%;display:flex;flex-direction:column;align-items:center;justify-content:center;gap:6px}
  .back-brand .lockup{display:flex;align-items:center;gap:10px}
  .back-brand .mark{width:30px;height:30px;border-radius:50%;background:var(--brand-orange)}
  .back-brand .wordmark{font-family:'Fredoka',sans-serif;font-weight:600;font-size:34px;color:var(--brand-blue);line-height:1}
  .back-brand .tagline{font-family:'Roboto',sans-serif;font-weight:500;font-size:13px;letter-spacing:1px;color:var(--brand-orange)}
  .divider{width:1px;height:180px;background:var(--rule)}
  .contact{padding-left:26px;font-family:'Roboto',sans-serif;color:var(--text-grey)}
  .contact .person{font-family:'Fredoka',sans-serif;font-weight:600;font-size:24px;color:var(--brand-blue);line-height:1}
  .contact .role{font-weight:500;font-size:15px;color:var(--brand-orange);margin-bottom:12px}
  .contact .address{font-size:14px;line-height:1.4;margin-bottom:8px}
  .contact ul{list-style:none;font-size:14px;line-height:1.55}
  .contact li{display:flex;align-items:center;gap:8px;white-space:nowrap}
  .contact svg{width:12px;height:12px;fill:var(--brand-blue);flex:none}
</style>
</head>
<body>
<main class="stage">
  <section class="card card--front">
    <div class="front-photo" role="img" aria-label="Photo of a smiling caregiver with an elderly woman seated by a bright window"></div>
    <div class="front-brand">
      <span class="mark"></span>
      <span class="wordmark">Velvet Days</span>
      <span class="website">www.velvetdays.example</span>
    </div>
  </section>

  <section class="card card--back">
    <div class="back-brand">
      <div class="lockup">
        <span class="mark"></span>
        <span class="wordmark">Velvet Days</span>
      </div>
      <span class="tagline">Caring for Seniors at Home</span>
    </div>
    <div class="divider"></div>
    <div class="contact">
      <p class="person">Daniel Reyes</p>
      <p class="role">CEO/Founder</p>
      <p class="address">2140 Willow Crest Road<br>Fairbanks, Alaska 99701</p>
      <ul>
        <li><svg viewBox="0 0 24 24" aria-hidden="true"><path d="M6.6 10.8a15.1 15.1 0 0 0 6.6 6.6l2.2-2.2a1 1 0 0 1 1-.25 11.4 11.4 0 0 0 3.6.57 1 1 0 0 1 1 1V20a1 1 0 0 1-1 1A17 17 0 0 1 3 4a1 1 0 0 1 1-1h3.5a1 1 0 0 1 1 1c0 1.25.2 2.45.57 3.57a1 1 0 0 1-.25 1z"/></svg>555 018 2743</li>
        <li><svg viewBox="0 0 24 24" aria-hidden="true"><path d="M2 5h20v14H2zm2 2v.5l8 5 8-5V7l-8 5z"/></svg>info@velvetdays.example</li>
        <li><svg viewBox="0 0 24 24" aria-hidden="true"><circle cx="12" cy="12" r="10"/></svg>www.velvetdays.example</li>
      </ul>
    </div>
  </section>
</main>
</body>
</html>
```